Bellwyn Strategic

Business Development Consulting Firm

Target Market(s)

Federal Government, 8(a) companies, Small Businesses

Industry/Entity Type

Private Sector, US Government

Contact Information for Business Card

8(a) Program Capture, Business Development, Industry Trends & Analysis, Strategic Teaming, Cyber Solutions

Colors

Designer to choose colors to be used in the design.

```html
<!DOCTYPE html>
<html lang="en">
<head>
<meta charset="utf-8">
<title>Bellwyn Strategic – Business Card</title>
<link rel="stylesheet" href="https://fonts.googleapis.com/css2?family=Poppins:wght@400;600&display=swap">
<style>
  :root {
    --page-bg: #e6e4e5;
    --card-light: #f4f1f2;
    --brand-blue: #0784cc;
    --brand-green: #6bb000;
    --text-on-blue: #ffffff;
  }
  * { margin: 0; padding: 0; box-sizing: border-box; }
  html, body { width: 1200px; height: 900px; overflow: hidden; }
  body { background: var(--page-bg); position: relative; }

  .business-card {
    position: absolute;
    left: 120px; top: 153px;
    width: 960px; height: 593px;
    display: flex;
    box-shadow: 0 10px 30px rgba(0,0,0,0.12);
  }
  .brand-side {
    width: 487px; height: 100%;
    background: var(--card-light);
    display: flex; flex-direction: column;
    align-items: center; justify-content: center;
    gap: 44px;
    padding-top: 30px;
  }
  .brand-dot {
    width: 54px; height: 54px; border-radius: 50%;
    background: var(--brand-green);
  }
  .brand-name {
    font-family: "Poppins", sans-serif;
    font-weight: 600;
    font-size: 32px;
    line-height: 1;
    color: var(--brand-blue);
  }
  .accent-stripe { width: 7px; height: 100%; background: var(--brand-green); }
  .contact-side {
    flex: 1; height: 100%;
    background: var(--brand-blue);
    color: var(--text-on-blue);
    font-family: "Poppins", sans-serif;
    padding: 108px 0 0 57px;
  }
  .person-name { font-weight: 600; font-size: 41px; line-height: 1.05; letter-spacing: 0.5px; }
  .person-title { font-size: 28px; line-height: 1.2; }
  .address { font-size: 28px; line-height: 35px; margin-top: 44px; }
  .contact-list { list-style: none; margin-top: 42px; font-size: 28px; line-height: 35px; }
  .contact-list li { display: flex; align-items: center; gap: 8px; }
  .contact-list svg { width: 26px; height: 26px; flex: none; }
</style>
</head>
<body>
  <div class="business-card">
    <section class="brand-side">
      <div class="brand-dot"></div>
      <div class="brand-name">Bellwyn Strategic</div>
    </section>
    <div class="accent-stripe"></div>
    <section class="contact-side">
      <h1 class="person-name">MARCUS HALE</h1>
      <p class="person-title">Managing Director</p>
      <p class="address">421, Address line<br>goes here<br>45452,Country Name</p>
      <ul class="contact-list">
        <li>
          <svg viewBox="0 0 24 24" aria-hidden="true"><path fill="#fff" d="M6.6 10.8a15.1 15.1 0 0 0 6.6 6.6l2.2-2.2c.3-.3.7-.4 1-.2 1.1.4 2.3.6 3.6.6.6 0 1 .4 1 1V20c0 .6-.4 1-1 1C10.6 21 3 13.4 3 4c0-.6.4-1 1-1h3.5c.6 0 1 .4 1 1 0 1.3.2 2.5.6 3.6.1.3 0 .7-.2 1z"/><path fill="none" stroke="#fff" stroke-width="1.8" d="M14 3.5a7 7 0 0 1 6.5 6.5M14 7a3.5 3.5 0 0 1 3 3"/></svg>
          <span>044-318 902 476</span>
        </li>
        <li>
          <svg viewBox="0 0 24 24" aria-hidden="true"><rect x="2" y="5" width="20" height="14" fill="#fff"/><path d="M2 5l10 8 10-8M2 19l7.5-7M22 19l-7.5-7" fill="none" stroke="var(--brand-blue)" stroke-width="1.6"/></svg>
          <span>hello@bellwyn.co</span>
        </li>
        <li>
          <svg viewBox="0 0 24 24" aria-hidden="true"><g fill="none" stroke="#fff" stroke-width="1.6"><circle cx="12" cy="12" r="10"/><ellipse cx="12" cy="12" rx="4.5" ry="10"/><path d="M2 12h20M4 6.5h16M4 17.5h16M12 2v20"/></g></svg>
          <span>www.bellwynstrategic.co</span>
        </li>
      </ul>
    </section>
  </div>
</body>
</html>
```